依頼詳細
新設法人の名刺デザインを依頼致します。
記載項目
表面:企業ロゴ、社名、肩書、氏名、住所、電話番号、FAX番号、携帯番号、
メールアドレス、ホームページアドレス
裏面:企業ロゴ、(キャッチコピー)
希望イメージ
シンプル 複雑
単色 カラフル
暗い 明るい
日常 高級
遊び心 厳粛
未来的 伝統的
女性的 男性的
希望する色
納品ファイル
• イラストレーター形式 (.ai)
• PNG形式 (.png)
補足説明
イラストレーター形式とネット印刷会社への入稿用にPDF形式も頂きたいです。

此方の要望にも柔軟に応じていただき、非常に良いデザインに仕上がりました。
背面のデザインが特に気に入っています。

この度は弊社のコンペに応募いただき、ありがとうございました。
どのデザインも非常に精度の高いものであり、選定に非常に悩みました。
また機会がございましたら、何卒よろしくお願い致します。

```html
<!DOCTYPE html>
<html lang="ja">
<head>
<meta charset="UTF-8">
<title>LUMIVA 名刺</title>
<link rel="stylesheet" href="https://fonts.googleapis.com/css2?family=Montserrat:wght@400;500&family=Noto+Sans+JP:wght@400;500;700&display=swap">
<style>
  :root {
    --page: #ffffff;
    --card: #ffffff;
    --card-edge: #bdbdbd;
    --ink: #2b2b2b;
    --band: #3d3d3d;
    --band-line: #6a6a6a;
    --band-label: #ffffff;
    --band-value: #a3a3a3;
  }
  * { margin: 0; padding: 0; box-sizing: border-box; }
  html, body { width: 900px; height: 1200px; overflow: hidden; background: var(--page); }
  body { position: relative; font-family: "Montserrat", "Noto Sans JP", sans-serif; color: var(--ink); }

  .card {
    position: absolute;
    left: 66px;
    width: 771px;
    background: var(--card);
    border: 2px solid var(--card-edge);
    overflow: hidden;
  }
  .card--back { top: 39px; height: 537px; }
  .card--front { top: 621px; height: 525px; }

  .top-block {
    position: absolute;
    left: 273px; top: 0;
    width: 225px; height: 126px;
    background: var(--band);
  }
  .brand-mark {
    position: absolute;
    left: 327px; top: 253px;
    width: 116px; height: 116px;
    border-radius: 50%;
    background: var(--ink);
  }
  .brand-name {
    position: absolute;
    left: 0; right: 0; top: 398px;
    text-align: center;
    font-family: "Montserrat", sans-serif;
    font-weight: 500;
    font-size: 42px;
    line-height: 1;
    letter-spacing: 2px;
    color: var(--ink);
  }
  .tagline {
    position: absolute;
    left: 0; right: 0; top: 446px;
    text-align: center;
    font-family: "Montserrat", sans-serif;
    font-weight: 500;
    font-size: 14px;
    line-height: 1;
    color: var(--ink);
  }

  .person-name {
    position: absolute;
    left: 0; right: 0; top: 80px;
    text-align: center;
    font-family: "Noto Sans JP", sans-serif;
    font-weight: 700;
    font-size: 38px;
    line-height: 1.2;
    letter-spacing: 3px;
  }
  .person-title {
    position: absolute;
    left: 0; right: 0; top: 134px;
    text-align: center;
    font-family: "Noto Sans JP", sans-serif;
    font-size: 14px;
    line-height: 1.2;
  }

  .contact-band {
    position: absolute;
    left: 0; right: 0; top: 190px;
    height: 198px;
    background: var(--band);
  }
  .divider-v {
    position: absolute;
    left: 383px; top: 30px;
    width: 1px; height: 135px;
    background: var(--band-line);
  }
  .divider-h {
    position: absolute;
    left: 100px; right: 100px; top: 98px;
    height: 1px;
    background: var(--band-line);
  }
  .contact {
    position: absolute;
    font-family: "Montserrat", sans-serif;
    line-height: 1.35;
  }
  .contact__label { display: block; font-size: 17px; font-weight: 500; color: var(--band-label); }
  .contact__value { display: block; font-size: 16px; color: var(--band-value); white-space: nowrap; }
  .contact--left { right: 437px; text-align: right; }
  .contact--right { left: 441px; text-align: left; }
  .row-1 { top: 40px; }
  .row-2 { top: 110px; }
  .contact-icon { position: absolute; width: 28px; height: 28px; }
  .icon-left { left: 340px; }
  .icon-right { left: 402px; }
</style>
</head>
<body>

<section class="card card--back">
  <div class="top-block"></div>
  <div class="brand-mark"></div>
  <div class="brand-name">LUMIVA</div>
  <div class="tagline">Good Products For You</div>
</section>

<section class="card card--front">
  <div class="person-name">名刺 太郎</div>
  <div class="person-title">代表取締役</div>

  <div class="contact-band">
    <div class="divider-v"></div>
    <div class="divider-h"></div>

    <div class="contact contact--left row-1">
      <span class="contact__label">Phone/Fax</span>
      <span class="contact__value">03-5550-2841/03-5550-2842</span>
    </div>
    <svg class="contact-icon icon-left" style="top:50px" viewBox="0 0 24 24" aria-hidden="true">
      <path fill="#fff" d="M6.6 10.8c1.4 2.8 3.8 5.1 6.6 6.6l2.2-2.2c.3-.3.7-.4 1-.2 1.1.4 2.3.6 3.6.6.6 0 1 .4 1 1V20c0 .6-.4 1-1 1C10.6 21 3 13.4 3 4c0-.6.4-1 1-1h3.5c.6 0 1 .4 1 1 0 1.3.2 2.5.6 3.6.1.3 0 .7-.2 1z"/>
    </svg>

    <div class="contact contact--left row-2">
      <span class="contact__label">Email</span>
      <span class="contact__value">info@lumiva.com</span>
    </div>
    <svg class="contact-icon icon-left" style="top:120px" viewBox="0 0 24 24" aria-hidden="true">
      <rect x="2" y="5" width="20" height="14" fill="#fff"/>
      <path d="M2.5 5.5 12 13l9.5-7.5" fill="none" stroke="#3d3d3d" stroke-width="1.6"/>
    </svg>

    <svg class="contact-icon icon-right" style="top:50px" viewBox="0 0 24 24" aria-hidden="true">
      <rect x="6.5" y="2" width="11" height="20" rx="1.5" fill="none" stroke="#fff" stroke-width="1.8"/>
      <rect x="8.5" y="5" width="7" height="12" fill="#fff"/>
    </svg>
    <div class="contact contact--right row-1">
      <span class="contact__label">Mobile</span>
      <span class="contact__value">090-5550-7316</span>
    </div>

    <svg class="contact-icon icon-right" style="top:120px" viewBox="0 0 24 24" aria-hidden="true">
      <path fill="#fff" d="M12 2a7 7 0 0 0-7 7c0 5.2 7 13 7 13s7-7.8 7-13a7 7 0 0 0-7-7zm0 9.5A2.5 2.5 0 1 1 12 6.5a2.5 2.5 0 0 1 0 5z"/>
    </svg>
    <div class="contact contact--right row-2">
      <span class="contact__label">Web</span>
      <span class="contact__value">www.lumiva.com</span>
    </div>
  </div>
</section>

</body>
</html>
```